Harborline Consultancy & Training Organization Web Site Design

Help!

We have started designing and building a Web site to promote and sell training services to HR managers. But we are not very good designers. In fact, we stink.

We have a logo.

We have most of the content (more or less) and the site architecture. But we have put together a pretty lousy look and feel.

Take a look: http://harborlinewise.example/pqvtlnwiseindex.html

What we'd like is a Web 3.0 type design - clean, simple, modern looking. Some sites we admire:

tilbrook.org
velquora.com
skorvane.com
brindlewords.com
ormak.com

We have access to stock photography, some of which we've used on the site we've built so far. You can use those and others. But keep it simple.

Target Market(s)

Professional HR managers in larger companies

Industry/Entity Type

Requirements
Must have
• Use our logo and a color scheme based off of it. Logo file uploaded.

Need to see home page and examples of secondary pages, based on site currently online.

```html
<!DOCTYPE html>
<html lang="en">
<head>
<meta charset="utf-8">
<title>Generations 101 – Harborline Matters</title>
<link href="https://fonts.googleapis.com/css2?family=Ubuntu+Condensed&family=Ubuntu:wght@400;500;700&display=swap" rel="stylesheet">
<style>
:root{
  --nav-top:#2f63c9;
  --nav-bottom:#163c96;
  --nav-active:#0c2766;
  --hero-light:#6f97e0;
  --hero-dark:#2e5fc4;
  --heading-blue:#7b9dc8;
  --link-blue:#2b8fd6;
  --text:#1e1e1e;
  --muted:#6b6b6b;
  --red:#d73535;
  --green:#6ccf5a;
  --orange:#f7962f;
  --tab-text:#d44040;
  --rule:#d5d5d5;
  --panel:#f6f6f6;
  --footer:#efefef;
  --white:#ffffff;
}
*{margin:0;padding:0;box-sizing:border-box}
html,body{width:674px;height:1200px;overflow:hidden;background:var(--white)}
body{font-family:"Ubuntu Condensed","Arial Narrow",sans-serif;color:var(--text)}
.page{position:relative;width:674px;height:1200px;overflow:hidden}

/* navigation */
.main-nav{position:absolute;left:0;top:0;width:674px;height:35px;background:linear-gradient(var(--nav-top),var(--nav-bottom));display:flex;align-items:center;justify-content:space-between;padding:0 18px 0 20px;white-space:nowrap}
.main-nav a{color:var(--white);text-decoration:none;font-size:12px;padding:3px 4px;border-radius:6px;white-space:nowrap}
.main-nav a.is-active{background:var(--nav-active)}

/* header */
.brand{position:absolute;left:26px;top:60px;display:flex;align-items:center;gap:8px;white-space:nowrap}
.brand-mark{width:24px;height:24px;border-radius:50%;background:var(--link-blue)}
.brand-name{font-family:"Ubuntu",sans-serif;font-weight:500;font-size:22px;color:#2a2a2a;letter-spacing:-.3px}
.contact{position:absolute;right:24px;top:54px;white-space:nowrap}
.contact-row{display:flex;align-items:center;gap:8px;height:22px}
.contact-phone{color:var(--link-blue);font-size:14px}
.contact-mail{color:var(--link-blue);font-size:10px;text-decoration:underline}

/* hero */
.hero{position:absolute;left:26px;top:107px;width:622px;height:161px;background:linear-gradient(90deg,var(--hero-dark),var(--hero-light) 70%);overflow:hidden}
.hero-photo{position:absolute;right:0;top:0;width:250px;height:161px;background:linear-gradient(90deg,rgba(255,255,255,0),#d9e2f0 35%,#b9c4d6)}
.hero-title{position:absolute;left:18px;top:46px;font-size:40px;color:var(--white);font-weight:400;white-space:nowrap;letter-spacing:-.3px}
.hero-sub{position:absolute;left:22px;top:95px;font-size:13px;color:var(--white);white-space:nowrap}

/* intro copy */
.intro{position:absolute;left:26px;top:285px;width:622px}
.section-title{font-family:"Ubuntu",sans-serif;font-weight:700;font-size:15px;line-height:20px;color:var(--heading-blue);letter-spacing:-.2px;margin-bottom:6px}
.intro p{font-size:9.2px;line-height:11px;margin-bottom:9px}
.intro .section-title.second{margin-top:8px}

/* generation tabs */
.gen-tabs{position:absolute;left:26px;top:596px;width:623px;height:27px;border-bottom:3px solid var(--rule);display:flex;gap:5px;padding-left:7px;background:var(--white)}
.gen-tab{width:106px;height:24px;border:1px solid var(--rule);border-bottom:none;background:linear-gradient(#ffffff,#f1f1f1);color:var(--tab-text);font-size:11px;display:flex;align-items:center;justify-content:center;white-space:nowrap}
.gen-tab.is-active{background:var(--white);height:25px}
.gen-photo{position:absolute;left:64px;top:626px;width:246px;height:157px;background:linear-gradient(#f3f4f6,#e2e5ea)}
.gen-facts{position:absolute;left:384px;top:654px;list-style:none;font-size:11px;text-transform:uppercase;white-space:nowrap}
.gen-facts li{height:32.5px}

/* columns */
.profile{position:absolute;left:26px;top:785px;width:517px;height:292px;display:flex;background:linear-gradient(var(--white),var(--panel));border:1px solid var(--rule);border-radius:0 0 6px 6px;overflow:hidden}
.profile-col{border-right:1px solid var(--rule)}
.profile-col:last-child{border-right:none}
.col-history{width:174px}
.col-icons{width:169px}
.col-attitudes{width:174px}
.profile-head{height:32px;color:var(--white);font-size:16px;font-weight:400;line-height:32px;padding-left:13px;white-space:nowrap;overflow:hidden}
.col-history .profile-head{background:var(--red);border-radius:5px 0 0 0}
.col-icons .profile-head{background:var(--green)}
.col-attitudes .profile-head{background:var(--orange);border-radius:0 5px 0 0}
.profile-list{list-style:none;padding:8px 8px 0 13px;font-size:10px;line-height:12px}
.profile-list li{min-height:22.8px;padding-bottom:4px}
.col-history .profile-list li,.col-icons .profile-list li{white-space:nowrap}
.profile-list b{font-weight:400;color:#000}
.profile-list i{font-style:italic}

/* footer */
.footer{position:absolute;left:0;top:1098px;width:674px;height:102px;background:var(--footer);border-top:1px solid #dcdcdc}
.footer-mark{position:absolute;left:36px;top:36px;width:26px;height:26px;border-radius:50%;background:var(--link-blue)}
.footer-nav{position:absolute;left:79px;top:20px;display:flex;gap:11px;font-size:8px;white-space:nowrap}
.footer-nav a{color:var(--muted);text-decoration:none}
.footer-nav a.is-active{color:var(--link-blue)}
.footer-copy{position:absolute;left:79px;top:39px;font-size:6px;color:var(--muted);white-space:nowrap}
.footer-rule{position:absolute;left:79px;top:56px;width:470px;border-top:1px solid #dadada}
.footer-about{position:absolute;left:79px;top:65px;width:300px;font-size:5.6px;line-height:12px;color:var(--muted)}
.social{position:absolute;left:526px;top:14px;display:flex;gap:3px}
.social span{width:24px;height:24px;border-radius:4px;background:#c9d3e0;color:#34507c;font-size:4px;display:flex;align-items:center;justify-content:center;overflow:hidden}
.chat{position:absolute;right:78px;top:64px;text-align:right;font-size:10px;white-space:nowrap}
.chat-q{color:#555}
.chat-cta{color:var(--red)}
.chat-icon{position:absolute;left:600px;top:66px}
</style>
</head>
<body>
<div class="page">

  <nav class="main-nav">
    <a class="is-active" href="#">HOME</a>
    <a href="#">ABOUT</a>
    <a href="#">GEN 101</a>
    <a href="#">GEN GAPS</a>
    <a href="#">STRATEGIES</a>
    <a href="#">RESOURCES</a>
    <a href="#">TRAINING</a>
    <a href="#">TOOLS</a>
    <a href="#">DISCUSS</a>
    <a href="#">CONTACT</a>
  </nav>

  <div class="brand">
    <span class="brand-mark"></span>
    <span class="brand-name">Harborline Matters …for Kestra</span>
  </div>

  <div class="contact">
    <div class="contact-row">
      <svg width="14" height="14" viewBox="0 0 14 14"><path d="M3 1 L5 1 L6 4 L4.5 5 C5 7 7 9 9 9.5 L10 8 L13 9 L13 11 C13 12 12 13 11 13 C5.5 13 1 8.5 1 3 C1 2 2 1 3 1Z" fill="none" stroke="#777" stroke-width="1"/></svg>
      <span class="contact-phone">888.415.2907</span>
    </div>
    <div class="contact-row">
      <svg width="14" height="10" viewBox="0 0 14 10"><rect x=".5" y=".5" width="13" height="9" fill="none" stroke="#777"/><path d="M.5 .5 L7 6 L13.5 .5" fill="none" stroke="#777"/></svg>
      <span class="contact-mail">info@harborlinewise.example</span>
    </div>
  </div>

  <section class="hero">
    <div class="hero-photo" role="img" aria-label="Photo of business professionals talking in an office"></div>
    <h1 class="hero-title">GENERATIONS 101</h1>
    <p class="hero-sub">Learn who the generations are and why they matter.</p>
  </section>

  <section class="intro">
    <h2 class="section-title">What are Generations 101?</h2>
    <p>Because each generation is unique, there is the potential for conflict that arises not from the actual position on any given issue, but on the generational values, perceptions, and stances associated with that issue. Knowing what makes generations distinct, as well as, knowing what binds all generations together help today’s manager to do the following:</p>
    <p>Because each generation is unique, there is the potential for conflict that arises not from the actual position on any given issue, but on the generational values, perceptions, and stances associated with that issue. Knowing what makes generations distinct, as well as, knowing what binds all generations together help today’s manager to do the following:</p>
    <h2 class="section-title second">Why Generations Matter:</h2>
    <p>Because each generation is unique, there is the potential for conflict that arises not from the actual position on any given issue, but on the generational values, perceptions, and stances associated with that issue. Knowing what makes generations distinct, as well as, knowing what binds all generations together help today’s manager to do the following:</p>
    <p>a. Resolve conflict faster based on understanding of the other person’s context.</p>
    <p>b. Capitalize on generational strengths while minimizing generational weakness.</p>
    <p>c. Delineate between personality conflict and generational conflict, which matters for reasons of influence and affinity throughout the company.</p>
    <p>d. Perceptions of fairness, performance, recruitment, motivation, incentive, and teaming are all highly influenced by generational characteristics.</p>
    <p>e. Market to a specific generation or cross-generationally – it allows for a greater chance of reaching the target effectively.</p>
  </section>

  <div class="gen-tabs">
    <span class="gen-tab is-active">MILLENNIAL</span>
    <span class="gen-tab">GEN X</span>
    <span class="gen-tab">BOOMER</span>
    <span class="gen-tab">SILENT</span>
  </div>

  <div class="gen-photo" role="img" aria-label="Photo of four young professionals in suits looking at their phones"></div>

  <ul class="gen-facts">
    <li>80 Million</li>
    <li>Born: 1983-2002</li>
    <li>Formative years: 1990-present</li>
    <li>Age in 2011: 28 and under</li>
  </ul>

  <section class="profile">
    <div class="profile-col col-history">
      <h3 class="profile-head">Historical influences</h3>
      <ul class="profile-list">
        <li>Internet</li><li>Globalization</li><li>Climate Change</li><li>Cell Phones</li>
        <li>Instant Messaging</li><li>Sillicon Valley</li><li>9/11</li><li>War in Iraq</li>
        <li>Vidstream</li><li>Friendwall</li><li>Reallity Tv</li>
      </ul>
    </div>
    <div class="profile-col col-icons">
      <h3 class="profile-head">Generational icons</h3>
      <ul class="profile-list">
        <li>Walter Henning (Sr. &amp; Jr.)</li><li>Carl Dunmore</li><li>Marcus Odell</li>
        <li>Lenny Paxton &amp; Sergei Varin</li><li>Daniel Pereth</li><li>Lorenzo Dellacroix</li>
        <li>Even Keel</li><li>Brianna Shields</li><li>Mitchell Fenwick</li><li>Selena Whitford</li>
      </ul>
    </div>
    <div class="profile-col col-attitudes">
      <h3 class="profile-head">Attitudes</h3>
      <ul class="profile-list">
        <li><b>Outlook:</b> <i>Confident</i></li>
        <li><b>Views Toward Authority:</b> <i>Uncertain</i></li>
        <li><b>View Leadership:</b> <i>Egalitarian</i></li>
        <li>Relationships: <i>Inclusive</i></li>
        <li>Work/life balance: <i>Integrated</i></li>
        <li>View of money: Mom? Dad? I borrow $20?</li>
      </ul>
    </div>
  </section>

  <footer class="footer">
    <span class="footer-mark"></span>
    <nav class="footer-nav">
      <a class="is-active" href="#">Home</a><a href="#">About</a><a href="#">Gen 101</a><a href="#">Gen Gaps</a>
      <a href="#">Strategies</a><a href="#">Resources</a><a href="#">Training</a><a href="#">Tools</a>
      <a href="#">Discuss</a><a href="#">Contact</a>
    </nav>
    <p class="footer-copy">All Rights Reserved - 2011. www.harborlinewise.example</p>
    <div class="footer-rule"></div>
    <p class="footer-about">Harborline Matters helps HR managers understand how each generation works, learns and leads. Our workshops, tools and coaching turn generational insight into clearer teams and fewer conflicts across the whole company.</p>
    <div class="social">
      <span>Friendwall</span><span>Chirpline</span><span>Linkory</span><span>Feedwell</span>
    </div>
    <div class="chat">
      <div class="chat-q">Questions?</div>
      <div class="chat-cta">CHAT WITH US!</div>
    </div>
    <svg class="chat-icon" width="30" height="22" viewBox="0 0 30 22">
      <ellipse cx="16" cy="9" rx="13" ry="8" fill="var(--orange)"/>
      <path d="M8 14 L4 21 L14 16Z" fill="var(--orange)"/>
    </svg>
  </footer>

</div>
</body>
</html>
```